Modern Business Card

Modern professional business card with more than just logo and demographic info. Something memorable.

We are a trendy/modern chiropractic group with an emphasis on neurology, hence the minimalist-type brain logo. We want to convey that modern and technical aspect with professionalism and the elite nature of our practice environment.

```html
<!DOCTYPE html>
<html lang="en">
<head>
<meta charset="utf-8">
<title>Vantage Chiropractic — Business Card</title>
<link rel="stylesheet" href="https://fonts.googleapis.com/css2?family=Caladea:ital,wght@0,400;0,700;1,400&display=swap">
<style>
  :root {
    --card-bg: #ffffff;
    --ink: #111111;
    --accent-blue: #4a7fc1;
    --trim-line: #1a1a1a;
  }
  html, body {
    margin: 0;
    padding: 0;
    width: 1200px;
    height: 720px;
    overflow: hidden;
    background: var(--card-bg);
  }
  .card {
    position: relative;
    width: 1200px;
    height: 720px;
    box-sizing: border-box;
    border: 2px solid var(--ink);
    background: var(--card-bg);
    font-family: "Caladea", "Cambria", Georgia, serif;
    color: var(--ink);
  }
  .trim-guides {
    position: absolute;
    inset: 0;
  }
  .brand {
    position: absolute;
    left: 100px;
    top: 100px;
    display: flex;
    align-items: center;
    gap: 34px;
  }
  .brand-square {
    width: 150px;
    height: 150px;
    background: var(--accent-blue);
  }
  .brand-name {
    margin: 0;
    font-weight: 400;
    color: var(--ink);
    line-height: 1;
    letter-spacing: 0.02em;
  }
  .brand-name .line-main {
    display: block;
    font-size: 108px;
  }
  .brand-name .line-sub {
    display: block;
    font-size: 60px;
    margin-top: 2px;
  }
  .contact {
    position: absolute;
    right: 72px;
    top: 372px;
    text-align: right;
    font-size: 30px;
    line-height: 44px;
  }
  .person-name {
    margin: 0;
    font-size: 48px;
    font-weight: 700;
    line-height: 56px;
    color: var(--accent-blue);
  }
  .person-title {
    margin: 0;
    font-style: italic;
    line-height: 40px;
  }
  .contact-line {
    margin: 0;
  }
  .label {
    font-weight: 700;
    color: var(--accent-blue);
  }
</style>
</head>
<body>
<div class="card">
  <svg class="trim-guides" width="1200" height="720" viewBox="0 0 1200 720" aria-hidden="true">
    <g fill="none" stroke="var(--trim-line)" stroke-width="2.5">
      <path d="M41 66 V42 H66"/>
      <path d="M1134 42 H1159 V66"/>
      <path d="M41 654 V678 H66"/>
      <path d="M1134 678 H1159 V654"/>
      <line x1="110" y1="42" x2="1100" y2="42" stroke-dasharray="42 42"/>
      <line x1="110" y1="678" x2="1100" y2="678" stroke-dasharray="42 42"/>
      <line x1="41" y1="110" x2="41" y2="620" stroke-dasharray="42 42"/>
      <line x1="1159" y1="110" x2="1159" y2="620" stroke-dasharray="42 42"/>
    </g>
  </svg>

  <div class="brand">
    <div class="brand-square" aria-hidden="true"></div>
    <h1 class="brand-name">
      <span class="line-main">VANTAGE</span>
      <span class="line-sub">CHIROPRACTIC</span>
    </h1>
  </div>

  <div class="contact">
    <p class="person-name">Name, Credentials</p>
    <p class="person-title">Title</p>
    <p class="contact-line"><span class="label">Cell</span> 000.000.0000 x0000 <span class="label">Fax</span> 000.000.0000 <span class="label">Pager</span> 000.000.0000</p>
    <p class="contact-line">Building Name | Suite #</p>
    <p class="contact-line">Address | City St, Zip</p>
    <p class="contact-line"><span class="label">Email</span> emailaddress@email.com | www.website.com</p>
  </div>
</div>
</body>
</html>
```